Restyle Company web site and logo

we need a wordpress design beacause after few year we need to refresh our company web site(www.vorantelabs.net) & logo. We are a small company called KP Advisory focused on business intellegence, data quality, data integration, etc and based on Legnago (small town near to Verona (italy)).
During the 2014 we add to our skill develop project for MDM and Procurement.
We are Young (avg 30 years old). We want to change our logo and color templete to communicate to all cumstomer professional skill, precision and passion.

--- UPDATE --
The new site can be complitile different from the actual website.
The new Logo is now available.
Updates

Target Market(s)

B2B, mid size market, professional account

Industry/Entity Type

It Company

Font styles to use
Sans Serif

Colors
acd037
3277b5

Requirements
Must have
• Simple and clean/clear image colur. Professional site. it need to rapresent trust site.
• Must be responsive desk/mobile.
Nice to have
• different color area for different kind off business line.
• slider image.
Should not have
• classical image

```html
<!DOCTYPE html>
<html lang="it">
<head>
<meta charset="utf-8">
<title>KP Advisory – Home</title>
<link rel="stylesheet" href="https://fonts.googleapis.com/css2?family=Titillium+Web:wght@300;400;600&family=Jost:wght@300&display=swap">
<style>
  :root{
    --lime:#9dc42a;
    --lime-soft:#b3d45a;
    --brand-blue:#1f6a9e;
    --hero-blue:#6b82b6;
    --ink:#2a5f8f;
    --grey-text:#8a8a8a;
    --white:#ffffff;
    --black:#000000;
  }
  *{box-sizing:border-box;margin:0;padding:0}
  html,body{width:1200px;height:1000px;overflow:hidden;background:var(--black)}
  body{position:relative;font-family:"Titillium Web",Arial,sans-serif}
  .site{position:absolute;left:0;top:0;width:620px;height:1000px;background:var(--white);overflow:hidden}
  .topbar{position:absolute;left:0;top:0;width:620px;height:18px;background:var(--lime)}
  .topbar .social{position:absolute;right:40px;top:1px;display:flex;gap:6px}
  .topbar .social span{width:14px;height:14px;border:1px solid rgba(255,255,255,.7);border-radius:50%}
  .masthead{position:absolute;left:0;top:18px;width:620px;height:126px;
    background:linear-gradient(100deg,#ffffff 0%,#f1f5f8 40%,#dbe4ec 75%,#e9eef2 100%)}
  .brand{position:absolute;left:86px;top:52px;display:flex;align-items:center;gap:8px}
  .brand .dot{width:14px;height:14px;border-radius:50%;background:var(--lime)}
  .brand .name{font-size:17px;font-weight:600;color:var(--ink);letter-spacing:.3px}
  .slogan{position:absolute;left:253px;top:32px;font-size:19px;line-height:23px;color:var(--ink);font-weight:400}
  .address{position:absolute;left:250px;top:97px;font-size:7.5px;color:var(--lime)}
  .mainnav{position:absolute;left:0;top:144px;width:620px;height:28px;background:var(--brand-blue);
    display:flex;justify-content:center;align-items:center;gap:20px;font-size:10px;color:var(--white)}
  .mainnav .active{color:var(--lime);border-bottom:1px solid var(--lime);padding-bottom:1px}
  .hero{position:absolute;left:0;top:172px;width:620px;height:208px;
    background:radial-gradient(circle at 170px 200px,#7c8fbc 0%,var(--hero-blue) 45%,#6479ae 100%);
    text-align:center;color:var(--white)}
  .hero h1{font-weight:300;font-size:22px;line-height:30px;color:var(--lime);margin-top:28px}
  .hero p{font-size:9.6px;line-height:17.5px;width:555px;margin:7px auto 0;font-weight:300}
  .hero-shadow{position:absolute;left:80px;top:376px;width:460px;height:10px;border-radius:50%;
    box-shadow:0 6px 10px rgba(0,0,0,.35)}
  .intro{position:absolute;left:26px;top:410px;width:564px;text-align:center}
  .intro h2{font-weight:400;font-size:16.5px;line-height:29px;color:var(--lime)}
  .intro p{margin-top:26px;font-size:9.8px;line-height:19px;color:var(--grey-text);text-align:justify;font-weight:300}
  .intro .claim{margin-top:14px;text-align:center;color:var(--lime);font-weight:600;font-size:9.5px}
  .news{position:absolute;top:607px;left:26px;display:flex;gap:22px}
  .card{width:122px;height:96px;background:var(--white);box-shadow:0 5px 8px rgba(0,0,0,.35)}
  .card .badge{height:60px;margin:0 2px;background:#d9d9d9}
  .card .badge.sky{background:linear-gradient(#4a9ad8,#7fbce8)}
  .card .badge.azure{background:#2f6fb3}
  .card h3{font-weight:400;font-size:9px;color:var(--lime);margin:6px 0 0 9px}
  .card time{display:block;font-size:8px;color:#aaa;margin-left:9px}
  .footer{position:absolute;left:0;top:765px;width:620px;height:172px;background:var(--lime);color:var(--white)}
  .col{position:absolute;top:16px;width:163px}
  .col h4{font-weight:400;font-size:11.5px;letter-spacing:1px;color:var(--ink);padding-bottom:6px;border-bottom:1px solid var(--white)}
  .col li{list-style:none;font-size:9px;height:28.5px;line-height:28px;border-bottom:1px solid var(--white)}
  .tags{display:flex;flex-wrap:wrap;gap:4px;margin-top:6px;width:165px}
  .tags span{background:var(--lime-soft);font-size:8.5px;padding:2px 6px;line-height:15.5px}
  .bottombar{position:absolute;left:0;top:937px;width:620px;height:63px;background:var(--brand-blue);
    display:flex;justify-content:center;align-items:center;gap:12px}
  .bottombar span{width:32px;height:32px;border-radius:7px;background:var(--lime)}
  .promo{position:absolute;left:620px;top:0;width:580px;height:1000px;background:var(--black);
    font-family:"Jost",Arial,sans-serif;font-weight:300;color:var(--lime);text-align:center;
    font-size:58px;line-height:77px;padding-top:45px}
</style>
</head>
<body>
  <div class="site">
    <div class="topbar"><div class="social"><span></span><span></span><span></span><span></span></div></div>
    <header class="masthead" role="img" aria-label="Soft light photo of office towers behind the header">
      <div class="brand"><span class="dot"></span><span class="name">KP Advisory</span></div>
      <div class="slogan">Put your company slogan here.<br>Comapny slogan words here.</div>
      <div class="address">Via delle Querce, 24 • 35092 Borgoselva (PD) • Tel 0429 – 5550192</div>
    </header>
    <nav class="mainnav">
      <span class="active">HOME ▾</span><span>BUSINESS PARTNERS</span><span>REFERENZE</span><span>CONTATTI</span>
      <svg width="9" height="9" viewBox="0 0 10 10"><circle cx="4" cy="4" r="3" fill="none" stroke="#9dc42a" stroke-width="1.5"/><line x1="6.2" y1="6.2" x2="9" y2="9" stroke="#9dc42a" stroke-width="1.5"/></svg>
    </nav>
    <section class="hero" role="img" aria-label="Blue toned photo of a performance gauge behind the headline">
      <h1>Corporate Performance Management (CPM)</h1>
      <p>E' un insieme di processi che aiutano le organizzazioni ad ottimizzare le prestazioni del business (viene visto come una Business Intelligence di nuova generazione). Si focalizza nei processi di business come la pianificazione e la previsione. Aiuta a scoprire utilizzi efficienti delle unità di business, finanziarie, umane, e risorse materiali al fine di ottenere la minimizzazione dei costi e di conseguenza massimizzare il ritorno degli investimenti. Coinvolge il consolidamento dei dati da varie sorgenti, la loro interrogazione, e l'analisi dei dati, mettendo in pratica i risultati.</p>
    </section>
    <div class="hero-shadow"></div>
    <section class="intro">
      <h2>Quante persone all'interno della vostra azienda hanno l'informazione desiderata,<br>nel momento giusto e nella forma corretta?</h2>
      <p>Per un'azienda è fondamentale sfruttare le innumerevoli informazioni di cui dispone rendendole consultabili ai propri manager al fine di aiutarli nella scelta delle giuste strategie aziendali (capire l'andamento delle performance dell'azienda, generare stime previsionali, ipotizzare scenari futuri e future strategie di risposta).</p>
      <p class="claim">KP Advisory vi aiuta a gestire questo processo nel modo più semplice e veloce!</p>
    </section>
    <div class="news">
      <article class="card"><div class="badge sky"></div><h3>News Article One</h3><time>OCTOBER 2, 2014</time></article>
      <article class="card"><div class="badge azure"></div><h3>News Article Two</h3><time>OCTOBER 2, 2014</time></article>
      <article class="card"><div class="badge"></div><h3>News Article Three</h3><time>OCTOBER 2, 2014</time></article>
      <article class="card"><div class="badge"></div><h3>News Article Four</h3><time>OCTOBER 1, 2014</time></article>
    </div>
    <footer class="footer">
      <div class="col" style="left:26px"><h4>NEWS</h4><ul><li>News Article One</li><li>News Article Two</li><li>News Article Three</li><li>News Article Four</li></ul></div>
      <div class="col" style="left:225px"><h4>CASE HISTORY</h4><ul><li>Case History 1</li><li>Case History 2</li><li>Case History 3</li><li>Case History 4</li></ul></div>
      <div class="col" style="left:424px"><h4>TAGS</h4>
        <div class="tags"><span>aziendali</span><span>panel</span><span>business</span><span>crystal</span><span>dati</span><span>NoraVale.Com</span><span>cloud</span><span>report</span><span>reports</span><span>software</span><span>utenti</span></div>
      </div>
    </footer>
    <div class="bottombar"><span></span><span></span><span></span><span></span></div>
  </div>
  <aside class="promo">See the test site at:<br>brightglyph.com/kp</aside>
</body>
</html>
```